Website for AV installation with booking system and e-commerce

Company: Corvexa
Tag Line: Audio Visual and Security System Installations
We need a website for an AV company based in Sydney Australia. We specialise in Audio Visual, CCTV (security cameras), and Data Cabling.
The purpose of the website is that customers book their installation online with a live booking system.
We are looking for the following:
- Creative and modern design
- easy to use - keep in mind that the user who will book will have little knowledge in technology.
- clean and organised
- colours to work in well with our logo we also like royal to navy blue, but we are open to other suggested what works well with our logo.
We want customers to be able to add products needed for their installation ie when booking to wall mount their TV they can choose to add a TV bracket and cables to the cart and vise-versa buy a bracket or cables and add to cart the installation.
Tabs to be included:
About us
Gallery
Contact Us
Home
Services (there are three services that we offer - Residential, Corporate and Retail)
Products
Book Online/Cart (checkout)
Temporary website checkout: www.corvexa.com.au, please note this is very basic and we do not want a copy of this. This is purely to give you an idea of our company.
Good Luck!
Target Market(s)
home owners/renters, business owners, archiects/designers, builders
Industry/Entity Type
E-Commerce
Look and feel

```html
<!DOCTYPE html>
<html lang="en">
<head>
<meta charset="utf-8">
<title>Corvexa – Audio Visual and Security System Installations</title>
<link href="https://fonts.googleapis.com/css2?family=Ubuntu:wght@400;500;700&display=swap" rel="stylesheet">
<style>
:root{
  --red:#d6121c;
  --dark:#111;
  --text:#555;
  --muted:#777;
  --footer:#2b2b2b;
  --footer-deep:#232323;
  --line:#e3e3e3;
  --green:#6fb52c;
}
*{margin:0;padding:0;box-sizing:border-box}
html,body{width:874px;height:1200px;overflow:hidden}
body{position:relative;background:#f2f2f2;font-family:"Ubuntu",sans-serif;color:var(--text)}
.abs{position:absolute}
/* header */
.site-header{position:absolute;left:0;top:0;width:874px;height:92px;background:#fff;border-top:3px solid #000;border-bottom:2px solid var(--red)}
.brand{position:absolute;left:80px;top:34px;display:flex;align-items:center;gap:8px;font-size:32px;font-weight:700;color:var(--red);letter-spacing:-0.5px}
.brand-dot{width:18px;height:18px;border-radius:50%;background:var(--red)}
.nav a{position:absolute;top:26px;font-size:10.5px;color:#222;text-decoration:none;text-align:center;transform:translateX(-50%);white-space:nowrap}
.nav svg{display:block;margin:0 auto 7px;width:12px;height:12px}
.nav .active{color:#222}
.nav-mark{position:absolute;left:314px;top:87px;width:45px;height:3px;background:var(--red)}
.nav-mark:after{content:"";position:absolute;left:18px;top:-5px;border:4px solid transparent;border-bottom-color:var(--red);border-top:0}
/* hero */
.hero{position:absolute;left:0;top:92px;width:874px;height:342px;background:linear-gradient(90deg,#000 0%,#050505 38%,#1b1b1d 62%,#2a2a2c 100%);border-bottom:2px solid var(--red);overflow:hidden}
.hero-photo{position:absolute;left:360px;top:0;width:514px;height:340px;background:radial-gradient(ellipse at 70% 35%,#8a1a22 0%,#3a1114 35%,#1a1a1c 70%,transparent 100%)}
.hero h1{position:absolute;left:81px;top:104px;font-size:33px;font-weight:500;color:#fff;line-height:35px;letter-spacing:-0.3px}
.hero-btn{position:absolute;left:82px;top:197px;width:168px;height:40px;background:linear-gradient(#3b3b3b,#111);color:#fff;font-size:13.5px;line-height:40px;padding-left:19px;border-radius:2px}
.dots{position:absolute;left:85px;top:245px;display:flex;gap:2px}
.dots i{width:7px;height:7px;border-radius:50%;background:var(--red)}
.dots i:first-child{background:#fff}
.hero-contact{position:absolute;left:602px;top:229px;font-size:10px;line-height:14.5px;color:#eee}
.hero-contact p+p{margin-top:14px}
/* content panel */
.panel{position:absolute;left:82px;top:456px;width:714px;height:510px;background:#fff;border:1px solid #e6e6e6;box-shadow:0 0 10px rgba(0,0,0,.08)}
.h-lg{position:absolute;font-size:19px;font-weight:500;color:#222;display:flex;align-items:center;gap:9px}
.h-md{position:absolute;font-size:12px;font-weight:500;color:#222;display:flex;align-items:center;gap:9px}
.rule{height:3px;border-top:1px dotted #ccc;border-bottom:1px dotted #ccc}
.service-img{position:absolute;top:50px;width:158px;height:127px}
.service-title{position:absolute;top:186px;font-size:12px;font-weight:500;color:#222}
.service-text{position:absolute;top:206px;width:156px;font-size:8.8px;line-height:11.4px;color:var(--muted)}
.support{position:absolute;left:542px;top:66px;display:flex;align-items:center;gap:6px;font-size:11px;color:var(--red)}
.support span.ic{width:19px;height:19px;border-radius:50%;background:var(--red);position:relative}
.support span.ic:after{content:"";position:absolute;left:5px;top:8.5px;width:9px;height:2px;background:#fff}
.why-text{position:absolute;left:542px;top:112px;width:150px;font-size:8px;line-height:13.8px;color:var(--muted)}
.bars{position:absolute;left:542px;top:162px;display:flex;gap:3px}
.bars i{height:3px;background:var(--green)}
.contact-list{position:absolute;left:544px;top:212px;font-size:10px;line-height:14.8px;color:var(--muted)}
.contact-list b{font-weight:500;color:#555;display:inline-block;width:11px}
.social{position:absolute;left:541px;top:263px;display:flex;gap:3px}
.social i{width:18px;height:18px;border-radius:50%}
.welcome-p{position:absolute;left:15px;width:440px;font-size:10px;line-height:13.1px;color:#555}
.read-more{position:absolute;left:15px;top:484px;font-size:10px;color:var(--red);text-decoration:underline}
.products-box{position:absolute;left:495px;top:329px;width:208px;height:157px;border:1px solid #e6e6e6;border-radius:2px}
.prod{position:absolute;left:9px;display:flex;gap:6px}
.prod-img{width:46px;height:52px}
.prod h4{font-size:11px;font-weight:500;color:#222}
.prod p{font-size:9px;line-height:11px;color:#555;margin-top:1px}
.prod .btns{margin-top:3px;display:flex;gap:3px}
.prod .btns span{background:#111;color:#fff;font-size:7.5px;padding:2px 4px}
.view-more{position:absolute;right:15px;top:146px;font-size:8px;color:var(--red);text-decoration:underline}
/* footer */
.site-footer{position:absolute;left:0;top:983px;width:874px;height:217px;background:var(--footer)}
.foot-h{position:absolute;top:16px;height:28px;border-top:1px solid #555;border-bottom:1px solid #555;font-size:12.5px;font-weight:500;color:#fff;text-align:center;line-height:26px}
.foot-h:after{content:"";position:absolute;left:50%;bottom:-1px;width:40px;margin-left:-20px;height:1px;background:var(--red)}
.foot-h:before{content:"";position:absolute;left:50%;top:-1px;width:40px;margin-left:-20px;height:1px;background:var(--red)}
.foot-links{position:absolute;left:98px;top:60px;list-style:none;font-size:9px;line-height:15px;color:#ddd}
.foot-text{position:absolute;font-size:9px;line-height:15.2px;color:#ccc}
.foot-bar{position:absolute;left:0;top:175px;width:874px;height:42px;background:var(--footer-deep)}
.copyright{position:absolute;left:100px;top:14px;font-size:8.5px;color:#bbb;font-family:Arial,sans-serif}
.foot-social{position:absolute;left:656px;top:10px;display:flex;gap:6px}
.foot-social i{width:18px;height:18px;border-radius:3px}
</style>
</head>
<body>

<header class="site-header">
  <div class="brand"><span class="brand-dot"></span>Corvexa</div>
  <nav class="nav">
    <a class="active" style="left:337px"><svg viewBox="0 0 12 12"><path d="M6 1 1 6h1.5v5h3V8h1v3h3V6H11z" fill="#d6121c"/></svg>HOME</a>
    <a style="left:400px"><svg viewBox="0 0 12 12"><path d="M1 2h10v8H1zM6 2v8" stroke="#222" fill="none" stroke-width="1.3"/></svg>About Us</a>
    <a style="left:465px"><svg viewBox="0 0 12 12"><rect x="1" y="2" width="10" height="8" fill="none" stroke="#222" stroke-width="1.3"/><path d="M2.5 9 5 6l2 2 1.5-1.5L10 9z" fill="#222"/></svg>Gallery</a>
    <a style="left:528px"><svg viewBox="0 0 12 12"><path d="M1 11V5l2 2V3l2 2V1l2 3v2l2-2v4l2-1v4z" fill="#222"/></svg>Services</a>
    <a style="left:595px"><svg viewBox="0 0 12 12"><rect x="1" y="3.5" width="10" height="7" fill="none" stroke="#222" stroke-width="1.3"/><path d="M4 3.5V2h4v1.5M1 6.5h10" stroke="#222" fill="none" stroke-width="1.2"/></svg>Products</a>
    <a style="left:667px"><svg viewBox="0 0 12 12"><rect x="1" y="2.5" width="10" height="7" fill="none" stroke="#222" stroke-width="1.3"/><path d="M1 2.5 6 7l5-4.5" stroke="#222" fill="none" stroke-width="1.2"/></svg>Contact Us</a>
    <a style="left:754px"><svg viewBox="0 0 12 12"><rect x="1.5" y="1.5" width="9" height="9" fill="none" stroke="#222" stroke-width="1.3"/><path d="M3 4h6M3 6h6M3 8h6" stroke="#222" stroke-width="1"/></svg>Booking Online</a>
  </nav>
  <div class="nav-mark"></div>
</header>

<section class="hero">
  <div class="hero-photo" role="img" aria-label="Close-up of red, white and yellow RCA audio cables plugged into the back of an AV receiver"></div>
  <h1>Audio Visual and Security<br>System Installations</h1>
  <div class="hero-btn">Learn More About Us</div>
  <div class="dots"><i></i><i></i><i></i><i></i></div>
  <div class="hero-contact">
    <p>Suite 12, 48 Harbour Ln,<br>Eastwick NSW 2099</p>
    <p>Email: hello@corvexa.com.au<br>Ph: (02) 9000 4120<br>Fax: (02) 9000 4125<br>Mobile: 0400 000 512</p>
  </div>
</section>

<main class="panel">
  <h2 class="h-lg" style="left:14px;top:14px;width:514px">Our Services <span class="rule" style="flex:1"></span></h2>

  <div class="service-img" style="left:15px;background:linear-gradient(135deg,#b9bdc0,#8e9296 60%,#3a3c3e)" role="img" aria-label="Living room with wall-mounted TV and lounge chair"></div>
  <div class="service-title" style="left:15px">Residential</div>
  <p class="service-text" style="left:15px">Lorem Ipsum is simply dummy text of the printing and typesetting indus-try. Lorem Ipsum has been the indus-try's standard dummy text</p>

  <div class="service-img" style="left:190px;background:linear-gradient(135deg,#5a4030,#2a1d16 60%,#4a6a8a)" role="img" aria-label="Corporate meeting room with large display screen"></div>
  <div class="service-title" style="left:190px">Corporate</div>
  <p class="service-text" style="left:190px">Lorem Ipsum is simply dummy text of the printing and typesetting indus-try. Lorem Ipsum has been the indus-try's standard dummy text</p>

  <div class="service-img" style="left:364px;background:linear-gradient(180deg,#8fa3b8,#5f7c4a 45%,#3a3a3a)" role="img" aria-label="Stadium control room with monitors overlooking the field"></div>
  <div class="service-title" style="left:364px">Retail</div>
  <p class="service-text" style="left:364px">Lorem Ipsum is simply dummy text of the printing and typesetting indus-try. Lorem Ipsum has been the indus-try's standard dummy text</p>

  <h3 class="h-md" style="left:542px;top:18px;width:164px">Why Choose Us <span class="rule" style="flex:1"></span></h3>
  <div class="support"><span class="ic"></span>Our Support Staff</div>
  <p class="why-text">Lorem Ipsum is simply dummy text of the printing and typesetting industry. Lorem Ipsum has been the industry's standard dummy</p>
  <div class="bars"><i style="width:40px"></i><i style="width:16px"></i><i style="width:22px"></i><i style="width:61px;background:#9bc526"></i></div>
  <h3 class="h-md" style="left:544px;top:184px">Contact Info</h3>
  <div class="contact-list">
    <div><b>T</b> (02) 9000 4120</div>
    <div><b>F</b> (02) 9000 4125</div>
    <div><b>M</b> hello@corvexa.com.au</div>
  </div>
  <div class="social">
    <i style="background:#3b5b9c"></i><i style="background:#2aa3d8"></i><i style="background:#d4452f"></i><i style="background:#c8202a"></i><i style="background:#7ab82a"></i><i style="background:#1e83b8"></i><i style="background:#ee7b24"></i>
  </div>

  <h2 class="h-lg" style="left:15px;top:306px;width:485px;font-size:16px">Welcome to Our Website <span class="rule" style="flex:1"></span></h2>
  <p class="welcome-p" style="top:337px">Corvexa is based in Sydney providing professional AV installation services for home and business. We have over 8 years experience in AV equipment and other electronic devices. We&nbsp; offer high quality services and can respond quickly to any job.</p>
  <p class="welcome-p" style="top:390px">It is a long established fact that a reader will be distracted by the readable content of a page when looking at its layout. The point of using Lorem Ipsum is that it has a more-or-less normal distribution of letters, as opposed to using 'Content here, content here', making it look like readable English. Many desktop publishing packages and web page editors now use Lorem Ipsum as their default model text, and a search for 'lorem ipsum' will uncover many web sites still in their infancy. Various versions have evolved over the years, sometimes by accident, sometimes on purpose (injected humour and the like).</p>
  <span class="read-more">Read More</span>

  <h3 class="h-md" style="left:496px;top:306px;width:210px">Our Products <span class="rule" style="flex:1"></span></h3>
  <div class="products-box">
    <div class="prod" style="top:9px">
      <div class="prod-img" style="background:linear-gradient(135deg,#2a8ac8,#c8202a 55%,#eee)" role="img" aria-label="Red and blue network cables"></div>
      <div><h4>Est qu'il possède une</h4><p>On sait depuis longtemps que<br>travailler avec.</p><div class="btns"><span>Details</span><span>Add to Cart</span></div></div>
    </div>
    <div class="prod" style="top:80px">
      <div class="prod-img" style="background:linear-gradient(135deg,#e8c878,#7a5a2a 55%,#222)" role="img" aria-label="Microphones on stands"></div>
      <div><h4>Est qu'il possède une</h4><p>On sait depuis longtemps que<br>travailler avec.</p><div class="btns"><span>Details</span><span>Add to Cart</span></div></div>
    </div>
    <span class="view-more">View More</span>
  </div>
</main>

<footer class="site-footer">
  <div class="foot-h" style="left:95px;width:106px">Links</div>
  <ul class="foot-links"><li>Home</li><li>Gallery</li><li>Services</li><li>Products</li><li>Contact Us</li></ul>

  <div class="foot-h" style="left:342px;width:104px">About Us</div>
  <p class="foot-text" style="left:342px;top:58px;width:170px">Corvexa is based in Sydney providing professional AV installation services for home and business. We have over 8 years experience in AV equipment and other electronic devices. We&nbsp; offer high quality services and can respond quickly to any job.</p>

  <div class="foot-h" style="left:651px;width:106px">Contact Info</div>
  <div class="foot-text" style="left:654px;top:59px;font-size:10px;line-height:14.5px">
    <p>Suite 12, 48 Harbour Ln,<br>Eastwick NSW 2099</p>
    <p style="margin-top:14px">Email: hello@corvexa.com.au<br>Ph: (02) 9000 4120<br>Fax: (02) 9000 4125<br>Mobile: 0400 000 512</p>
  </div>

  <div class="foot-bar">
    <div class="copyright">Copyright 2013 corvexa.com</div>
    <div class="foot-social"><i style="background:#2aa3d8"></i><i style="background:#3b5b9c"></i><i style="background:#c8202a"></i><i style="background:#d4452f"></i></div>
  </div>
</footer>

</body>
</html>
```